Editorial Website Design for High-End Custom Millwork Firm

Design (no development) for a 5-7 page website for a high-end custom architectural millwork firm. Editorial, magazine-quality aesthetic — think Dwelling Quarterly and top-tier millwork studios (Owen Tallard, Vorko). Full brief, reference sites, and project photography attached. We have uploaded a sample of our photography to use in your design. PLEASE READ PDF DOCUMENT BRIEF!!!

```html
<!DOCTYPE html>
<html lang="en">
<head>
<meta charset="utf-8">
<title>Alder Row Millwork</title>
<link rel="stylesheet" href="https://fonts.googleapis.com/css2?family=Gilda+Display&family=Inter:wght@400;500;600&display=swap">
<style>
:root{
  --paper:#f4f1ea;
  --white:#ffffff;
  --ink:#1d1c1a;
  --muted:#5d5851;
  --line:#2a2826;
  --accent:#a69583;
  --accent-text:#9a8876;
}
*{box-sizing:border-box;margin:0;padding:0}
html,body{width:1200px;height:4880px;overflow:hidden}
body{position:relative;background:var(--white);color:var(--ink);font-family:"Inter",sans-serif}
.serif{font-family:"Gilda Display",serif}
.abs{position:absolute}
.band{position:absolute;left:0;width:1200px}
.paper{background:var(--paper)}
.photo{position:absolute}
.btn{position:absolute;display:flex;align-items:center;justify-content:center;gap:12px;background:var(--accent);color:#fff;font-family:"Gilda Display",serif;text-transform:uppercase;letter-spacing:.04em;font-size:15px}
.btn.small{font-size:10px;gap:8px}
.btn svg{width:14px;height:10px}
.btn.small svg{width:10px;height:8px}
.hline{position:absolute;height:1.5px;background:var(--line)}
.vline{position:absolute;width:1.5px;background:var(--line)}
h1,h2,h3{font-weight:400}
.section-title{position:absolute;font-family:"Gilda Display",serif;font-size:52px;line-height:1}
.section-note{position:absolute;font-size:13px;line-height:1.75;color:var(--ink)}
.list{position:absolute;list-style:none}
.list li{height:53px;border-bottom:1.5px solid var(--line);display:flex;align-items:center;font-size:13.5px;font-weight:500;padding-left:33px}
.list li.active{background:var(--white)}
.eyebrow{position:absolute;font-size:9px;letter-spacing:.04em;text-transform:uppercase;color:var(--accent-text)}
.card-title{position:absolute;font-family:"Gilda Display",serif;font-size:25px}
.body-copy{position:absolute;font-size:12px;line-height:1.72;color:var(--ink)}
.statement{position:absolute;font-family:"Gilda Display",serif;line-height:1.12}
.footer h4{position:absolute;font-family:"Gilda Display",serif;font-weight:400;font-size:16px}
.footer p{position:absolute;font-size:11px;line-height:1.6;color:var(--ink)}
.footer .label{font-size:9px;font-weight:600}
.footer .link{color:var(--accent-text);font-size:12px}
</style>
</head>
<body>

<!-- hero -->
<header class="band paper" style="top:0;height:667px"></header>
<div class="photo" role="img" aria-label="Bright kitchen with pale oak cabinetry, marble backsplash and a runner rug leading to an open door" style="left:601px;top:0;width:599px;height:667px;background:linear-gradient(160deg,#e9e4dc 0%,#d7c6aa 45%,#b99a72 75%,#8b7b68 100%)"></div>
<div class="abs serif" style="left:0;top:0;width:102px;height:46px;background:var(--accent);color:#fff;font-size:30px;letter-spacing:.12em;display:flex;align-items:center;justify-content:center">ARM</div>
<div class="abs" style="left:1153px;top:0;width:47px;height:46px;background:var(--white);display:flex;align-items:center;justify-content:center">
  <svg width="16" height="12" viewBox="0 0 16 12"><path d="M0 1h16M0 6h16M0 11h16" stroke="#1d1c1a" stroke-width="1.5"/></svg>
</div>
<h1 class="abs serif" style="left:67px;top:210px;font-size:70px;line-height:1.08">Design Space<br>People Love</h1>
<p class="abs" style="left:67px;top:386px;font-size:15px">Handcrafted in the heart of Durham, North California</p>
<a class="btn" style="left:68px;top:453px;width:180px;height:52px">Contact us <svg viewBox="0 0 14 10"><path d="M0 5h12M8 1l4 4-4 4" fill="none" stroke="#fff" stroke-width="1.3"/></svg></a>
<div class="hline" style="left:0;top:666px;width:1200px"></div>
<div class="vline" style="left:600px;top:0;height:730px"></div>

<!-- intro -->
<p class="statement" style="left:200px;top:778px;width:800px;text-align:center;font-size:30px;line-height:1.13">Working with the top designers and architects on the east coast to produce and install high end millwork in residential and commercial environments.</p>

<!-- commercial -->
<section class="band paper" style="top:938px;height:867px"></section>
<h2 class="section-title" style="left:180px;top:1000px">Alder Commercial</h2>
<p class="section-note" style="left:611px;top:1002px;width:410px">Utilizing our capabilities and knowledge as a resource for architects and interior design</p>
<div class="photo" role="img" aria-label="Retail store interior with arched display shelving and a round central table" style="left:180px;top:1092px;width:418px;height:374px;background:linear-gradient(135deg,#4a3a2c 0%,#a07a52 40%,#d9c2a0 60%,#3b3a38 100%)"></div>
<div class="hline" style="left:599px;top:1091px;width:421px"></div>
<ul class="list" style="left:599px;top:1092px;width:421px">
  <li>Corporate</li><li>Performing arts</li><li>Museums</li><li>Academic</li><li class="active">Retail</li><li>Residential</li><li>Exterior</li>
</ul>
<span class="eyebrow" style="left:180px;top:1507px">Latest case study</span>
<h3 class="card-title" style="left:180px;top:1536px">Wexford Store Retail</h3>
<p class="body-copy" style="left:180px;top:1576px;width:400px">Maecenas varius, tellus ac dapibus dictum, tellus mi interdum purus, id consequat ipsum velit at tortor. Cras ac odio facilisis, congue nisi eu, porttitor diam. Aenean ullamcorper ornare gravida. In sodales, est consectetur dignissim pellentesque</p>
<a class="btn small" style="left:180px;top:1687px;width:141px;height:32px">Read the story <svg viewBox="0 0 14 10"><path d="M0 5h12M8 1l4 4-4 4" fill="none" stroke="#fff" stroke-width="1.3"/></svg></a>
<div class="photo" role="img" aria-label="Store reception with wood counter, wall map and coffered ceiling lights" style="left:631px;top:1505px;width:389px;height:234px;background:linear-gradient(120deg,#3d3128 0%,#8a6b4c 45%,#c9b79b 70%,#4e4438 100%)"></div>

<!-- residential -->
<h2 class="section-title" style="left:180px;top:1866px">Alder Residential</h2>
<p class="section-note" style="left:611px;top:1868px;width:410px">We draw on this area's history of fine furniture making and have attracted skilled craftsmen</p>
<div class="hline" style="left:180px;top:1956px;width:840px"></div>
<ul class="list" style="left:180px;top:1957px;width:418px">
  <li class="paper" style="background:var(--paper)">Boardroom</li><li style="background:var(--paper)">Dining</li><li style="background:var(--paper)">Desk</li><li style="background:var(--paper)">Cabinetry</li><li style="background:var(--paper)">Kitchen</li>
</ul>
<div class="hline" style="left:180px;top:2329px;width:840px"></div>
<div class="vline" style="left:598px;top:1957px;height:373px"></div>
<div class="photo" role="img" aria-label="White kitchen with oak island and pendant lights" style="left:600px;top:1958px;width:420px;height:371px;background:linear-gradient(170deg,#f2efe9 0%,#e2dbd0 55%,#b9956d 80%,#d8cfc3 100%)"></div>
<div class="photo" role="img" aria-label="White kitchen with island seating and glass pendant lamps" style="left:180px;top:2370px;width:389px;height:233px;background:linear-gradient(175deg,#f0ede7 0%,#ddd6cb 60%,#7d6a58 90%)"></div>
<span class="eyebrow" style="left:631px;top:2372px">Product lines</span>
<h3 class="card-title" style="left:631px;top:2402px">Discover Our Product Lines</h3>
<p class="body-copy" style="left:631px;top:2442px;width:395px">Maecenas varius, tellus ac dapibus dictum, tellus mi interdum purus, id consequat ipsum velit at tortor. Cras ac odio facilisis, congue nisi eu, porttitor diam. Aenean ullamcorper ornare gravida. In sodales, est consectetur dignissim pellentesque</p>
<a class="btn small" style="left:631px;top:2554px;width:160px;height:31px">Our product lines <svg viewBox="0 0 14 10"><path d="M0 5h12M8 1l4 4-4 4" fill="none" stroke="#fff" stroke-width="1.3"/></svg></a>

<!-- workshop -->
<section class="band paper" style="top:2673px;height:599px"></section>
<div class="hline" style="left:0;top:2672px;width:1200px"></div>
<div class="hline" style="left:0;top:3271px;width:1200px"></div>
<div class="photo" role="img" aria-label="Craftsman assembling a lattice panel frame on a workshop bench" style="left:0;top:2673px;width:677px;height:599px;background:linear-gradient(140deg,#6b6257 0%,#b5aa98 35%,#d9d2c3 55%,#7e7a73 100%)"></div>
<div class="vline" style="left:677px;top:2673px;height:599px"></div>
<div class="abs" style="left:749px;top:2806px;width:44px;height:44px;border-radius:50%;background:#3a3835"></div>
<div class="abs" style="left:800px;top:2814px;width:66px;height:28px;background:#8c8882"></div>
<div class="abs" style="left:895px;top:2806px;width:44px;height:44px;border-radius:50%;background:#8c8882"></div>
<p class="statement" style="left:749px;top:2880px;width:420px;font-size:31px">We put the full power of our knowledge, facilities, and craftsmanship to work for you in the most cost-effective way possible.</p>
<a class="btn" style="left:749px;top:3087px;width:190px;height:46px;font-size:13px">Our capabilities <svg viewBox="0 0 14 10"><path d="M0 5h12M8 1l4 4-4 4" fill="none" stroke="#fff" stroke-width="1.3"/></svg></a>

<!-- about -->
<p class="statement" style="left:180px;top:3335px;width:700px;font-size:30px">Our firm was established in 1988 and is located in historic Durham, North Carolina. We are a Minority Owned Business (Certified MBE)</p>
<a class="btn" style="left:180px;top:3473px;width:134px;height:44px;font-size:13px">About us <svg viewBox="0 0 14 10"><path d="M0 5h12M8 1l4 4-4 4" fill="none" stroke="#fff" stroke-width="1.3"/></svg></a>
<div class="photo" role="img" aria-label="Two craftsmen reviewing drawings at a workshop table" style="left:172px;top:3640px;width:205px;height:167px;background:linear-gradient(150deg,#5b4a38 0%,#a99277 50%,#6d6257 100%)"></div>
<div class="photo" role="img" aria-label="Worker in face shield grinding metal with sparks" style="left:389px;top:3587px;width:204px;height:220px;background:linear-gradient(160deg,#cfc8bb 0%,#8f8a84 50%,#3f4550 100%)"></div>
<div class="photo" role="img" aria-label="Craftsman sanding a curved wooden frame in the shop" style="left:605px;top:3545px;width:413px;height:262px;background:linear-gradient(130deg,#3a3631 0%,#8a7a66 40%,#d2c0a4 65%,#5c544b 100%)"></div>

<!-- insight -->
<section class="band paper" style="top:3877px;height:516px"></section>
<h2 class="section-title" style="left:180px;top:3940px">Latest Insight</h2>
<div class="abs" style="left:826px;top:3949px;width:32px;height:32px;border:1px solid #cfc9bf;display:flex;align-items:center;justify-content:center"><svg width="12" height="10" viewBox="0 0 14 10"><path d="M14 5H2M6 1L2 5l4 4" fill="none" stroke="#b5aea3" stroke-width="1.3"/></svg></div>
<div class="abs" style="left:863px;top:3949px;width:32px;height:32px;border:1.5px solid var(--ink);display:flex;align-items:center;justify-content:center"><svg width="12" height="10" viewBox="0 0 14 10"><path d="M0 5h12M8 1l4 4-4 4" fill="none" stroke="#1d1c1a" stroke-width="1.3"/></svg></div>
<a class="btn small" style="left:910px;top:3949px;width:110px;height:32px">View more <svg viewBox="0 0 14 10"><path d="M0 5h12M8 1l4 4-4 4" fill="none" stroke="#fff" stroke-width="1.3"/></svg></a>

<div class="photo" role="img" aria-label="Kitchen island with pendant lights and marble wall" style="left:180px;top:4033px;width:264px;height:199px;background:linear-gradient(170deg,#ebe6de 0%,#d8cbb6 55%,#a88c6a 100%)"></div>
<span class="eyebrow" style="left:180px;top:4262px;font-size:8px">Latest project</span>
<p class="abs" style="left:180px;top:4286px;width:264px;font-size:14.5px;font-weight:500;line-height:1.3">Curabitur vulputate urna massa. Nulla libero magna</p>

<div class="photo" role="img" aria-label="Lounge with blue sofa and carved wood screen panels" style="left:466px;top:4033px;width:264px;height:199px;background:linear-gradient(150deg,#6d4a2e 0%,#b88c5a 40%,#3f4670 70%,#8a6a4a 100%)"></div>
<span class="eyebrow" style="left:466px;top:4262px;font-size:8px">Impact</span>
<p class="abs" style="left:466px;top:4286px;width:264px;font-size:14.5px;font-weight:500;line-height:1.3">Etiam imperdiet, elit fermentum tempus posuere</p>

<div class="photo" role="img" aria-label="Wet bar with walnut cabinets and glass-front upper cabinets" style="left:755px;top:4033px;width:265px;height:199px;background:linear-gradient(175deg,#d8d2c8 0%,#a56b3c 50%,#5e3620 100%)"></div>
<span class="eyebrow" style="left:755px;top:4262px;font-size:8px">Latest project</span>
<p class="abs" style="left:755px;top:4286px;width:265px;font-size:14.5px;font-weight:500;line-height:1.3">Etiam imperdiet, elit fermentum tempus posuere</p>

<!-- call to action -->
<div class="hline" style="left:0;top:4393px;width:1200px"></div>
<div class="vline" style="left:743px;top:4393px;height:205px"></div>
<p class="statement" style="left:180px;top:4452px;width:500px;font-size:35px;line-height:1.1">Looking right partner for your dream project?</p>
<a class="btn" style="left:840px;top:4469px;width:180px;height:50px;font-size:15px">Contact us <svg viewBox="0 0 14 10"><path d="M0 5h12M8 1l4 4-4 4" fill="none" stroke="#fff" stroke-width="1.3"/></svg></a>
<div class="hline" style="left:0;top:4597px;width:1200px"></div>

<!-- footer -->
<footer class="band paper footer" style="top:4598px;height:282px">
  <h4 style="left:180px;top:58px">Alder Row Millwork.</h4>
  <p style="left:180px;top:102px">Alder Row is a Minority Owned Business.<br>A Certified MBE.</p>
  <p style="left:180px;top:152px">All Rights Reserved. Alder Row Millwork.</p>

  <h4 style="left:611px;top:58px">Visit Us</h4>
  <p style="left:611px;top:102px">1140 Ferrow Street<br>Durham, NC 27701</p>
  <p class="link" style="left:611px;top:150px">Get Directions</p>

  <h4 style="left:827px;top:58px">Contact Us</h4>
  <p class="label" style="left:827px;top:100px">Phone</p>
  <p class="link" style="left:827px;top:116px">919.555.0142</p>
  <p class="label" style="left:827px;top:148px">Fax</p>
  <p class="link" style="left:827px;top:164px">919.555.0187</p>
  <p class="label" style="left:827px;top:196px">Email</p>
  <p class="link" style="left:827px;top:212px">info@aldermillwork.com</p>
</footer>

</body>
</html>
```